Mexican Themed Party Invitations!

Hi,
We are wanting a Mexican themed party invititation for Derek's 40th!
We are wanting something that resembles an old Mexican postcard – like the ones you used to get in the 50’s–70's - the size would approximately be 7" by 5.5".
We would preferably like a double sided invite - The below details would be displayed on the back somewhere:
If there could also be room left somewhere on the back to attach a small magnet so that the invite can be stuck on the fridge:)
Derek's 40th
When: Saturday the 27th of July 2013 @ 7PM
Where: 48 Farrow Terrace, Coromandel Valley, SA
Bring: Yourself and cowboy drinkin’ boots
RSVP: Date, email and phone – make funny RSVP email address!
Dress: Preferably traditional Mexican or 70’s Cowboy/Girl – but tacky Sombrero’s and Ponchos are OK too!
Men: There will be a prize for the best grown (real) Mexican moustache
Music: by the Dusty Spurs, Mexican Mariachi Band
Food: Supplied by……
Drinks: Bartender Neville will have the tequila shots and sangria ready to go
RSVP: by the 1st of July
Please note that we have attached some examples of pictures that we like as a bit of inspiration to give you a bit of an idea of which direction we are wanting to go in.
70's style would be good as Derek was born then.
We can't wait to see what you come up with!!!
Updates
Just for some inspration I found this image, which I love! If someone could do something like this, that would be awesome!
http://www.bids.pebblecart.com/stuff/k/k_chh_tolova_greet_57260.jpg
Paco's 40th insted of Tolova (or similar)

```html
<!DOCTYPE html>
<html lang="en">
<head>
<meta charset="utf-8">
<title>Derek's Fortieth – Invitation</title>
<link rel="stylesheet" href="https://fonts.googleapis.com/css2?family=Alfa+Slab+One&family=Yellowtail&family=Shadows+Into+Light+Two&family=Oswald:wght@500&display=swap">
<style>
  :root {
    --page: #ffffff;
    --card-peach: #f6dccb;
    --card-cream: #fcefe6;
    --ink: #3b2a26;
    --chili: #b63a2c;
    --chili-light: #f3d7c7;
    --header-peach: #e8b8a0;
    --rule: #4a3a36;
    --postmark: #d0524a;
    --stamp-edge: #fffaf4;
  }
  * { box-sizing: border-box; margin: 0; padding: 0; }
  html, body { width: 1200px; height: 900px; overflow: hidden; background: var(--page); }
  .canvas { position: relative; width: 1200px; height: 900px; }

  /* ---------- front ---------- */
  .card-front {
    position: absolute; left: 300px; top: 6px; width: 600px; height: 432px;
    background: var(--card-peach); padding: 14px;
    box-shadow: 0 1px 3px rgba(0,0,0,.12);
  }
  .front-photo {
    position: relative; width: 100%; height: 100%; overflow: hidden;
    background:
      radial-gradient(ellipse at 30% 75%, rgba(70,150,120,.55), transparent 45%),
      radial-gradient(ellipse at 82% 65%, rgba(40,50,80,.7), transparent 40%),
      radial-gradient(ellipse at 60% 60%, rgba(200,70,50,.45), transparent 40%),
      linear-gradient(180deg, #8f8a82 0%, #b9aea0 45%, #a69382 100%);
  }
  .welcome-sign {
    position: absolute; left: 232px; top: 8px; width: 110px; height: 20px;
    background: #5f7d86; color: #e9e2d6;
    font: 500 11px/20px "Oswald", sans-serif; letter-spacing: 2px; text-align: center;
  }
  .front-name {
    position: absolute; left: 28px; top: 26px;
    font: 36px/1 "Yellowtail", cursive; color: #fff;
    transform: rotate(-8deg);
  }
  .front-title {
    position: absolute; left: 100px; top: 46px;
    font: 60px/1 "Alfa Slab One", serif; color: var(--chili);
    letter-spacing: 2px;
    -webkit-text-stroke: 2px var(--chili-light); paint-order: stroke fill;
  }
  .front-banner {
    position: absolute; right: 20px; bottom: 20px;
    padding: 2px 14px; background: #efe4d2; color: var(--ink);
    font: 22px/1.1 "Yellowtail", cursive; transform: rotate(-4deg);
    border: 1px solid #8b7b6a;
  }

  /* ---------- back ---------- */
  .card-back {
    position: absolute; left: 300px; top: 464px; width: 600px; height: 432px;
    background: var(--card-cream); padding: 10px;
    box-shadow: 0 1px 3px rgba(0,0,0,.12);
  }
  .back-frame {
    position: relative; width: 100%; height: 100%;
    border: 1.5px solid var(--rule); border-radius: 10px;
  }
  .back-divider {
    position: absolute; left: 288px; top: 18px; bottom: 30px;
    border-left: 1.5px solid var(--rule);
  }
  .back-heading {
    position: absolute; left: 22px; top: 18px;
    font: 26px/1 "Alfa Slab One", serif; color: var(--header-peach); letter-spacing: 1px;
  }
  .details {
    position: absolute; left: 22px; top: 84px; width: 250px;
    font: 13px/1.45 "Shadows Into Light Two", cursive; color: var(--ink);
    list-style: none;
  }
  .details li { margin-bottom: 17px; }
  .postmark { position: absolute; left: 364px; top: 14px; }
  .stamp {
    position: absolute; left: 486px; top: 14px; width: 64px; height: 88px;
    background: var(--stamp-edge); padding: 5px;
    border: 2px dotted #d9cabd;
  }
  .stamp-label, .stamp-value {
    font: 500 6px/1 "Oswald", sans-serif; color: var(--ink); text-align: center; letter-spacing: .5px;
  }
  .stamp-art {
    width: 100%; height: 58px; margin: 3px 0;
    background: radial-gradient(circle at 50% 55%, #c7a36a, #a8683e 60%, #6e4a34);
  }
  .address-lines { position: absolute; left: 308px; top: 214px; width: 262px; list-style: none; }
  .address-lines li {
    height: 46px; border-bottom: 1.5px solid var(--rule);
    display: flex; align-items: flex-end; padding-bottom: 4px;
    font: 15px/1.2 "Shadows Into Light Two", cursive; color: var(--ink);
  }
</style>
</head>
<body>
<main class="canvas">

  <section class="card-front">
    <div class="front-photo" role="img" aria-label="Vintage colour photograph of dancers in traditional Mexican folk costume outside an adobe building">
      <div class="welcome-sign">WELCOME TO</div>
      <div class="front-name">Derek's</div>
      <h1 class="front-title">FORTIETH</h1>
      <div class="front-banner">Hello Coromandel</div>
    </div>
  </section>

  <section class="card-back">
    <div class="back-frame">
      <h2 class="back-heading">FORTIETH</h2>
      <ul class="details">
        <li>Dress: Preferably traditional Mexican or 70's Cowboy/Girl – but tacky Sombrero's and Ponchos are OK too!</li>
        <li>Men: There will be a prize for the best grown (real) Mexican moustache</li>
        <li>Music by the Dusty Spurs, Mexican Mariachi Band</li>
        <li>Food: Supplied by……</li>
        <li>Drinks: Bartender Neville will have the tequila shots and sangria ready to go</li>
        <li>RSVP: by the 1st of July</li>
      </ul>

      <div class="back-divider"></div>

      <svg class="postmark" width="96" height="96" viewBox="0 0 96 96" aria-label="Postmark dated July 27 1973">
        <defs><path id="ring" d="M48 48 m-34 0 a34 34 0 1 1 68 0 a34 34 0 1 1 -68 0"/></defs>
        <circle cx="48" cy="48" r="42" fill="none" stroke="var(--postmark)" stroke-width="2"/>
        <circle cx="48" cy="48" r="26" fill="none" stroke="var(--postmark)" stroke-width="1.5"/>
        <text font-family="Oswald, sans-serif" font-size="9" fill="var(--postmark)" letter-spacing="2">
          <textPath href="#ring" startOffset="2%">CORREO • FIESTA</textPath>
        </text>
        <text x="48" y="42" text-anchor="middle" font-family="Oswald, sans-serif" font-size="9" fill="var(--postmark)">JUL</text>
        <text x="48" y="54" text-anchor="middle" font-family="Oswald, sans-serif" font-size="12" fill="var(--postmark)">27</text>
        <text x="48" y="64" text-anchor="middle" font-family="Oswald, sans-serif" font-size="8" fill="var(--postmark)">1973</text>
        <text x="48" y="84" text-anchor="middle" font-family="Oswald, sans-serif" font-size="8" fill="var(--postmark)">POST</text>
      </svg>

      <div class="stamp">
        <div class="stamp-label">CORREO DE FIESTA</div>
        <div class="stamp-art" role="img" aria-label="Vintage postage stamp illustration"></div>
        <div class="stamp-value">30</div>
      </div>

      <ul class="address-lines">
        <li>Saturday, 27th of July 2013 @ 7pm</li>
        <li>48 Farrow Terrace, Coromandel Valley, SA</li>
        <li>Bring yourself &amp; cowboy drinkin' boots</li>
        <li>RSVP date, email and phone</li>
      </ul>
    </div>
  </section>

</main>
</body>
</html>
```